Property Management business needs Business cards designed

We provide a premium property management service based in Sydney's Norther Beaches. We want people to feel confident in choosing us to manage their investment properties. We offer a much more personalized service than other estate agents.
We want a modern clean design. Something that shows confidence without being complicated.
Logo attached.

Target Market(s)

35-70yo Male and Female with strong property portfolios within Sydney's Norther Beaches

Industry/Entity Type

Property Management

Contact Information for Business Card

Address: Suite 7, 12-14 Kelvin Parade, Harlow NSW 2188
Two separate named cards.
Tom Ardley - 0491 570 118 tom@harbourvaleestates.com.au
Clara Dunmore - 0491 570 263 clara@harbourvaleestates.com.au

Requirements
Must have
• Business logo, name, number, address, email.

```html
<!DOCTYPE html>
<html lang="en">
<head>
<meta charset="utf-8">
<title>Harbourvale Estates — Business Cards</title>
<link rel="stylesheet" href="https://fonts.googleapis.com/css2?family=Roboto+Condensed:wght@400;600&display=swap">
<style>
  :root {
    --backdrop: #ddd9d4;
    --card: #ffffff;
    --ink: #2b2b2b;
    --ink-soft: #3a3a3a;
    --teal: #2a7d87;
  }
  * { box-sizing: border-box; margin: 0; padding: 0; }
  html, body { width: 1200px; height: 900px; overflow: hidden; }
  body {
    background: var(--backdrop);
    font-family: "Roboto Condensed", "Arial Narrow", sans-serif;
    color: var(--ink);
    position: relative;
  }
  .card {
    position: absolute;
    width: 442px;
    height: 259px;
    background: var(--card);
    border-radius: 18px;
    box-shadow: 0 2px 6px rgba(0,0,0,0.12);
  }
  .card--front-clara { left: 130px; top: 162px; }
  .card--front-tom   { left: 628px; top: 162px; }
  .card--back-clara  { left: 130px; top: 504px; }
  .card--back-tom    { left: 628px; top: 504px; }

  .brand {
    position: absolute;
    display: flex;
    align-items: center;
    gap: 8px;
    font-weight: 600;
    font-size: 20px;
    letter-spacing: 0.2px;
    color: var(--ink);
    white-space: nowrap;
  }
  .brand__mark {
    width: 12px; height: 12px;
    background: var(--teal);
    flex: none;
  }
  .card--front-clara .brand,
  .card--front-tom .brand { right: 25px; top: 47px; }
  .card--back-clara .brand,
  .card--back-tom .brand { left: 33px; top: 118px; font-size: 19px; }

  .holder-name {
    font-size: 18px;
    font-weight: 400;
    color: var(--ink);
  }
  .front .holder-name {
    position: absolute;
    right: 25px;
    top: 154px;
    text-align: right;
  }
  .front .rule {
    position: absolute;
    left: 27px;
    right: 25px;
    top: 180px;
    height: 3px;
    background: var(--teal);
  }
  .front .address {
    position: absolute;
    left: 27px;
    top: 188px;
    font-size: 10px;
    color: var(--ink-soft);
  }
  .contact {
    font-size: 8px;
    line-height: 12px;
    color: var(--ink-soft);
    list-style: none;
  }
  .front .contact { position: absolute; left: 27px; top: 207px; }

  .back .holder-name { position: absolute; left: 265px; top: 54px; }
  .back .contact { position: absolute; left: 271px; top: 108px; }
  .back .address {
    position: absolute;
    left: 271px;
    top: 184px;
    font-size: 8px;
    line-height: 11px;
    color: var(--ink-soft);
  }
</style>
</head>
<body>

  <article class="card front card--front-clara">
    <div class="brand"><span class="brand__mark"></span>HARBOURVALE ESTATES</div>
    <h2 class="holder-name">Clara Dunmore</h2>
    <div class="rule"></div>
    <p class="address">Suite 7, 12-14 Kelvin Parade, Harlow NSW 2188</p>
    <ul class="contact">
      <li>T : 0491 570 263</li>
      <li>E : clara@harbourvaleestates.com.au</li>
    </ul>
  </article>

  <article class="card front card--front-tom">
    <div class="brand"><span class="brand__mark"></span>HARBOURVALE ESTATES</div>
    <h2 class="holder-name">Tom Ardley</h2>
    <div class="rule"></div>
    <p class="address">Suite 7, 12-14 Kelvin Parade, Harlow NSW 2188</p>
    <ul class="contact">
      <li>T : 0491 570 118</li>
      <li>E : tom@harbourvaleestates.com.au</li>
    </ul>
  </article>

  <article class="card back card--back-clara">
    <div class="brand"><span class="brand__mark"></span>HARBOURVALE ESTATES</div>
    <h2 class="holder-name">Clara Dunmore</h2>
    <ul class="contact">
      <li>T : 0491 570 263</li>
      <li>E : clara@harbourvaleestates.com.au</li>
    </ul>
    <p class="address">Suite 7, 12-14 Kelvin Parade<br>Harlow NSW 2188</p>
  </article>

  <article class="card back card--back-tom">
    <div class="brand"><span class="brand__mark"></span>HARBOURVALE ESTATES</div>
    <h2 class="holder-name">Tom Ardley</h2>
    <ul class="contact">
      <li>T : 0491 570 118</li>
      <li>E : tom@harbourvaleestates.com.au</li>
    </ul>
    <p class="address">Suite 7, 12-14 Kelvin Parade<br>Harlow NSW 2188</p>
  </article>

</body>
</html>
```